Tech Startup Needs Business Card Design

I am looking for an eye catching business card design for our new company, Torn Kite. We are a place for business owners and contractors to share their experiences with their customers and check their current customers. Our website, www.torn-kite.co, may be able to offer some guidance as to the design.

Industry/Entity Type

Business

Contact Information for Business Card

Owen Barthwick
888-417-3083
Owen@torn-kite.co
www.torn-kite.co

```html
<!DOCTYPE html>
<html lang="en">
<head>
<meta charset="utf-8">
<title>Torn Kite — Business Cards</title>
<link rel="stylesheet" href="https://fonts.googleapis.com/css2?family=Poppins:wght@500;600&family=Arimo:ital,wght@0,400;0,700;1,400&display=swap">
<style>
  :root {
    --red: #e8202a;
    --red-dark: #c9151f;
    --ink: #111111;
    --grey: #555555;
    --paper: #ffffff;
    --backdrop: #e9e6e1;
  }
  * { box-sizing: border-box; margin: 0; padding: 0; }
  html, body { width: 1200px; height: 950px; overflow: hidden; }
  body {
    background: var(--backdrop);
    font-family: "Arimo", Arial, sans-serif;
    position: relative;
  }
  .card {
    position: absolute;
    left: 250px;
    width: 700px;
    height: 400px;
    background: var(--paper);
    box-shadow: 0 6px 18px rgba(0,0,0,.18);
    overflow: hidden;
  }
  .card-back { top: 55px; }
  .card-front { top: 495px; }

  /* back */
  .back-brand {
    position: absolute;
    left: 0; right: 0; top: 140px;
    display: flex; align-items: center; justify-content: center; gap: 14px;
  }
  .brand-dot {
    width: 34px; height: 34px; border-radius: 50%;
    background: var(--red);
  }
  .brand-name {
    font-family: "Poppins", Arial, sans-serif;
    font-weight: 600;
    color: var(--red);
    letter-spacing: -1px;
    line-height: 1;
  }
  .back-brand .brand-name { font-size: 52px; }
  .back-url {
    position: absolute;
    left: 0; right: 0; top: 268px;
    text-align: center;
    font-size: 15px;
    letter-spacing: 3px;
    color: var(--grey);
  }

  /* front */
  .wave { position: absolute; inset: 0; width: 700px; height: 400px; }
  .person {
    position: absolute;
    right: 34px; top: 118px;
    text-align: right;
    color: var(--paper);
  }
  .person-name { font-weight: 700; font-size: 21px; }
  .person-title { font-style: italic; font-size: 17px; margin-top: 4px; }

  .front-brand {
    position: absolute;
    left: 60px; top: 195px;
    display: flex; align-items: center; gap: 12px;
  }
  .front-brand .brand-dot { width: 30px; height: 30px; }
  .front-brand .brand-name { font-size: 56px; color: var(--ink); }

  .contacts {
    position: absolute;
    left: 40px; right: 30px; bottom: 42px;
    display: flex; justify-content: space-between;
    font-size: 16px; color: #333;
  }
  .contact { display: flex; align-items: center; gap: 7px; }
  .contact svg { width: 16px; height: 16px; fill: var(--red); }
</style>
</head>
<body>

<section class="card card-back">
  <div class="back-brand">
    <span class="brand-dot"></span>
    <span class="brand-name">tornkite</span>
  </div>
  <p class="back-url">www.torn-kite.co</p>
</section>

<section class="card card-front">
  <svg class="wave" viewBox="0 0 700 400" aria-hidden="true">
    <path d="M0 0 H700 V285 C590 280 500 215 420 140 C330 55 170 25 0 38 Z" fill="var(--red)"/>
    <path d="M40 100 C150 50 290 48 360 95 C280 68 160 72 40 100 Z" fill="var(--ink)"/>
    <path d="M395 160 C470 235 560 272 700 262" fill="none" stroke="var(--paper)" stroke-width="5"/>
  </svg>

  <div class="person">
    <p class="person-name">Owen Barthwick</p>
    <p class="person-title">President</p>
  </div>

  <div class="front-brand">
    <span class="brand-dot"></span>
    <span class="brand-name">tornkite</span>
  </div>

  <div class="contacts">
    <span class="contact">
      <svg viewBox="0 0 16 16"><path d="M3 1h3l1.5 4-2 1.3a9 9 0 0 0 4.2 4.2L11 8.5l4 1.5v3a2 2 0 0 1-2 2A12 12 0 0 1 1 3a2 2 0 0 1 2-2z"/></svg>
      888-417-3083
    </span>
    <span class="contact">
      <svg viewBox="0 0 16 16"><path d="M1 3h14v10H1z M1 3l7 6 7-6" fill="var(--red)" stroke="#fff" stroke-width="1.2"/></svg>
      Owen@torn-kite.co
    </span>
    <span class="contact">
      <svg viewBox="0 0 16 16"><circle cx="8" cy="8" r="7"/><path d="M1 8h14M8 1c3 3 3 11 0 14M8 1c-3 3-3 11 0 14" fill="none" stroke="#fff" stroke-width="1"/></svg>
      www.torn-kite.co
    </span>
  </div>
</section>

</body>
</html>
```